New Design Real Estate Platform - Products

We need a new PowerPoint presentation for our real estate platform products B2B area. The colors should be in the company logo. New graphics are also welcome. Some information or images (placeholders) are still missing. It should be a modern design that is clear.

Requirements
Must have
• graphics for facts & figure, new graphics in general

```html
<!DOCTYPE html>
<html lang="de">
<head>
<meta charset="utf-8">
<title>Baufeld Portal AG – Produkte</title>
<link href="https://fonts.googleapis.com/css2?family=Montserrat:ital,wght@0,600;0,700;0,800;1,500;1,700&family=Open+Sans:wght@400;600;700&display=swap" rel="stylesheet">
<style>
:root{
  --green:#76c00f;
  --green-dark:#2f5e0a;
  --ink:#1d1d1b;
  --text:#333;
  --grey-bg:#e4e5e6;
  --row:#e7e7e7;
  --row-alt:#f3f3f3;
  --dark:#1e1e1e;
  --white:#fff;
}
*{box-sizing:border-box;margin:0;padding:0}
html,body{width:1200px;height:731px;overflow:hidden}
body{background:var(--grey-bg);font-family:"Open Sans",sans-serif;color:var(--text);position:relative}
.slide{position:absolute;width:362px;height:204px;background:var(--white);box-shadow:0 2px 5px rgba(0,0,0,.18);overflow:hidden}
.c1{left:43px}.c2{left:419px}.c3{left:796px}
.r1{top:47px}.r2{top:266px}.r3{top:484px}
.abs{position:absolute}
.title{position:absolute;left:14px;top:10px;font-family:"Montserrat",sans-serif;font-weight:800;font-size:12px;color:var(--ink)}
.title-bar{position:absolute;left:14px;top:28px;width:26px;height:2px;background:var(--green)}
.subtitle{position:absolute;left:14px;top:34px;font-family:"Montserrat",sans-serif;font-weight:700;font-size:6.2px;color:var(--ink)}
.footer{position:absolute;left:6px;right:12px;bottom:6px;height:12px}
.footer .mark{position:absolute;left:0;top:0;width:11px;height:11px;border:1.2px solid var(--green);border-radius:50%}
.footer .info{position:absolute;left:15px;top:4px;font-size:2.6px;font-weight:600;color:var(--ink);letter-spacing:.1px}
.footer .line{position:absolute;left:80px;right:8px;top:6px;height:.4px;background:#999}
.footer .num{position:absolute;right:0;top:3.5px;font-size:3.6px;font-weight:700;color:var(--ink)}
.ph{position:absolute}
.green{color:var(--green)}
b{font-weight:700}

/* slide 1 */
.s1-brand{position:absolute;left:18px;font-family:"Montserrat",sans-serif;color:var(--ink);display:flex;align-items:center;gap:4px}
.s1-brand .dot{width:15px;height:15px;border:2px solid var(--green);border-radius:50%}
.s1-brand .sq{width:13px;height:11px;background:#2a7fd3}
.s1-head{position:absolute;left:22px;top:84px;font-family:"Montserrat",sans-serif;font-weight:800;color:var(--ink);line-height:1.05}
.s1-head .l1{font-size:13.5px}
.s1-head .l2{font-size:20px;color:var(--green)}
.s1-head .l3{font-size:13.5px}
.s1-sub{position:absolute;left:22px;top:148px;font-family:"Montserrat",sans-serif;font-style:italic;font-weight:500;font-size:8px;line-height:1.3;color:var(--ink)}
.s1-dots{position:absolute;left:22px;top:184px;display:flex;gap:4px}
.s1-dots i{width:4px;height:4px;border-radius:50%;background:var(--ink)}
.s1-dots i:nth-child(2){background:var(--green)}
.s1-band{position:absolute;left:152px;right:0;top:165px;bottom:0;background:var(--green);color:var(--white);font-family:"Montserrat",sans-serif;font-weight:700;font-size:13px;display:flex;align-items:center;justify-content:center}

/* bullets */
.bullets{list-style:none;font-size:4.6px;line-height:1.55;color:var(--ink)}
.bullets li{position:relative;padding-left:4px;margin-bottom:7.5px}
.bullets li::before{content:"";position:absolute;left:0;top:2.4px;width:1.6px;height:1.6px;border-radius:50%;background:var(--green)}

/* slide 3 */
.chart{position:absolute;left:36px;top:44px;width:100px;height:69px;border-radius:3px;box-shadow:0 0 3px rgba(0,0,0,.2);background:var(--white)}
.chart .t{position:absolute;left:0;right:0;top:3px;text-align:center;font-size:3.4px;font-weight:700;color:var(--ink)}
.p3-text{position:absolute;left:20px;top:120px;width:131px;font-size:4.2px;line-height:1.5;text-align:justify;color:var(--ink)}
.gcard{position:absolute;top:31px;width:72px;height:143px;background:var(--green);border-radius:5px;color:var(--white)}
.gcard .img{position:absolute;left:3px;right:3px;top:3px;height:43px;border-radius:3px}
.gcard h4{position:absolute;left:6px;top:52px;font-size:5px;font-weight:700}
.gcard ul{position:absolute;left:6px;right:4px;top:60px;list-style:none;font-size:4px;line-height:1.45}
.gcard li{position:relative;padding-left:3.5px;margin-bottom:1px}
.gcard li::before{content:"";position:absolute;left:0;top:2px;width:1.5px;height:1.5px;border-radius:50%;background:var(--white)}

/* slide 4 */
.pp{position:absolute;top:46px;width:54px;text-align:center}
.pp svg{display:block;margin:0 auto;height:22px}
.pp .lbl{margin-top:4px;font-family:"Montserrat",sans-serif;font-weight:700;font-style:italic;font-size:6.6px;color:var(--ink)}
.pp .box{margin-top:3px;height:52px;border:1px solid var(--green-dark);font-size:3.8px;line-height:1.35;padding:2px;color:var(--ink)}
.p4-bar{position:absolute;left:35px;top:148px;width:290px;height:20px;background:var(--dark);color:var(--white);font-size:4.2px;line-height:1.5;text-align:center;padding-top:3px}

/* slide 5 tables */
table.prod{position:absolute;left:26px;width:310px;border-collapse:separate;border-spacing:.5px;font-size:3.6px;text-align:center;color:var(--ink)}
table.prod th{background:var(--green);color:var(--white);font-weight:700;height:12px;line-height:1.1;font-size:3.8px}
table.prod td{background:var(--row);height:11px;line-height:1.1}
table.prod tr:nth-child(even) td{background:var(--row-alt)}
table.prod td:first-child{text-align:left;padding-left:1px}

/* slide 6 */
.p6-box{position:absolute;left:40px;top:83px;width:109px;height:55px;background:var(--green);color:var(--white);font-size:5.2px;line-height:1.55;padding:5px 8px;text-align:justify}
.p6-sq{position:absolute;left:36px;top:80px;width:6px;height:6px;background:#000}

/* slide 7 */
.p7-dark{position:absolute;left:239px;top:54px;width:103px;height:118px;background:var(--dark);border-radius:5px;color:var(--white);font-size:5.2px;line-height:1.4;padding:10px 7px;text-align:justify}
.p7-dark p{margin-bottom:9px}
.p7-dark .green{font-weight:700}

/* slide 8/9 text */
.side{position:absolute;font-size:5.2px;line-height:1.35;color:var(--ink)}
.side p{margin-bottom:7px}
.side .green{font-weight:600}
.shot{position:absolute;box-shadow:0 1px 4px rgba(0,0,0,.3)}
</style>
</head>
<body>

<!-- Slide 1: Cover -->
<section class="slide c1 r1">
  <div class="s1-brand" style="top:20px;font-size:9px;font-weight:600;font-style:italic"><span class="dot"></span>wohnneu.ch</div>
  <div class="s1-brand" style="top:48px;font-size:10px;font-weight:600"><span class="sq"></span>NEUZUG</div>
  <div class="s1-head"><div class="l1">Der Match</div><div class="l2">Maker im</div><div class="l3">Neubau-Bereich</div></div>
  <div class="s1-sub">Ihr Angebot &amp; unsere<br>Nachfrage!</div>
  <div class="s1-dots"><i></i><i></i><i></i></div>
  <div class="ph" role="img" aria-label="Photo: handshake above small model houses on a desk" style="left:152px;top:0;right:0;height:165px;background:linear-gradient(160deg,#d9dde2 0%,#a9b2bd 45%,#7f7a73 100%)"></div>
  <div class="s1-band">Baufeld Portal AG</div>
</section>

<!-- Slide 2: Facts & Figures -->
<section class="slide c2 r1">
  <div class="title">Facts &amp; Figures</div><div class="title-bar"></div>
  <ul class="bullets abs" style="left:28px;top:44px;width:152px">
    <li>Nischenportal spezialisiert auf Neubauten</li>
    <li>Zahlenden Abonnenten sind effektiv auf der Suche nach Wohneigentum / Mietobjekten und haben oft die Finanzierung geklärt = hoch qualifizierte Anfragen</li>
    <li>Verlinkung der Projektwebsite im Inserat = keine ständigen Updates im Inserat nötig</li>
    <li>Wir sammeln die Interessenten für Sie und geben Ihnen die Kontaktdaten zum korrekten Zeitpunkt= keine verfrühten &amp; ständige Anfragen</li>
    <li>Interessenten werden laufend informiert, so stellen wir sicher das die Kunden zufrieden sind.</li>
  </ul>
  <div class="abs" style="left:190px;top:37px;width:.5px;height:132px;background:#999"></div>
  <ul class="bullets abs" style="left:203px;top:44px;width:150px">
    <li>2.0 Mio-&gt;Unique-Besucher p.a. auf unseren beiden Portalen wohnneu.ch und neuzug.ch</li>
    <li>4000+-&gt; Zahlende Abonnenten mit Suchprofilen</li>
    <li>Zahlen</li><li>Zahlen</li><li>Zahlen</li><li>Zahlen</li>
  </ul>
  <div class="footer"><span class="mark"></span><span class="info">Baufeld Portal AG | info@baufeldportal.ch</span><span class="line"></span><span class="num">2</span></div>
</section>

<!-- Slide 3: Plattform -->
<section class="slide c3 r1">
  <div class="title">Unsere Plattform</div><div class="title-bar"></div>
  <div class="chart">
    <div class="t">Anzahl exklusive Neubauobjekte</div>
    <svg class="abs" style="left:0;top:0" width="100" height="69" viewBox="0 0 100 69">
      <line x1="50" y1="9" x2="50" y2="64" stroke="#222" stroke-width=".5"/>
      <line x1="6" y1="36" x2="82" y2="36" stroke="#222" stroke-width=".5"/>
      <rect x="12" y="39" width="20" height="4" rx="1" fill="#c9c9c9"/>
      <rect x="18" y="46" width="14" height="3" rx="1" fill="#c9c9c9"/>
      <rect x="20" y="52" width="14" height="3" rx="1" fill="#c9c9c9"/>
      <rect x="62" y="54" width="26" height="5" fill="var(--green)"/>
      <circle cx="66" cy="13" r="2" fill="none" stroke="var(--green)" stroke-width=".6"/>
      <rect x="70" y="12" width="22" height="2" fill="#555"/>
      <rect x="64" y="19" width="3" height="2" fill="#2a7fd3"/><rect x="69" y="19" width="15" height="2" fill="#555"/>
    </svg>
    <div class="abs" style="left:78px;top:32px;font-size:2.6px;line-height:1.1;color:#222;text-align:right">Kostenloses<br>Inserieren</div>
  </div>
  <p class="p3-text">Mit uns inserieren Sie Ihre Neubauprojekte <span class="green">exklusiv und kostenlos</span> – auf dem <span class="green">führenden Nischenportal</span> der Schweiz. Dank dem kostenpflichtigen Such-Abo für Interessenten erhalten Sie <span class="green">qualifizierte Anfragen</span> und <span class="green">schaffen Effizienz</span> im Vermarktungsprozess! Unsere Plattform gliedert sich in zwei Bereiche ein, einen <span class="green">geschlossenen Bereich</span> bei welchem nur unsere Abonnenten Zugang haben sowie einem <span class="green">öffentlichen Bereich</span> wo alle Interessenten Suchen können.</p>
  <div class="gcard" style="left:169px">
    <div class="img" role="img" aria-label="Screenshot: project card in the pre-marketing area" style="background:linear-gradient(135deg,#f3ecd6,#d8c28e)"></div>
    <h4>Vorvermarktung</h4>
    <ul><li>kostenloses Inserieren</li><li>Sichtbar nur für zahlende Abonnenten</li><li>Qualifizierte Anfragen</li><li>Evaluierung des Marktes</li></ul>
  </div>
  <div class="gcard" style="left:259px">
    <div class="img" role="img" aria-label="Screenshot: project card in the public area" style="background:linear-gradient(135deg,#fafafa,#c9b9a6)"></div>
    <h4>Öffentlicher Bereich</h4>
    <ul><li>Projekt sichtbar für alle Suchenden</li><li>wenn Ihr Projekt bereits in der Vorvermarkung bei uns war, läuft das Inserat kostenlos für Sie im öffentlichen Bereich weiter</li><li>Kostenpflichtig, wenn das Projekt nicht bei uns in der Vorvermarktung war.</li></ul>
  </div>
  <div class="footer"><span class="mark"></span><span class="info">Baufeld Portal AG | info@baufeldportal.ch</span><span class="line"></span><span class="num">3</span></div>
</section>

<!-- Slide 4: Premium-Partnerschaft -->
<section class="slide c1 r2">
  <div class="title">Premium-Partnerschaft</div><div class="title-bar"></div>
  <div class="pp" style="left:35px">
    <svg viewBox="0 0 30 22"><path d="M2 9l7-5 6 4 6-4 7 5-8 8-5-3-5 3z" fill="var(--green-dark)"/></svg>
    <div class="lbl">“Vereinbarung”</div>
    <div class="box">Wir schliessen eine gemeinsame Partnerschaft nach dem <b>“Geben und Nehmen Prinzip”</b> ab.</div>
  </div>
  <div class="pp" style="left:94px">
    <svg viewBox="0 0 30 22"><rect x="3" y="2" width="24" height="4" fill="var(--green-dark)"/><rect x="3" y="9" width="24" height="4" fill="var(--green-dark)"/><rect x="3" y="16" width="24" height="4" fill="var(--green-dark)"/></svg>
    <div class="lbl">“Geben”</div>
    <div class="box">Sie <b>inserieren</b> neue Projekte immer mind. <b>4 Wochen</b> vor dem offiziellen <b>Vermarktungsstart</b> exklusiv und <b>kostenlos</b> auf wohnneu.ch und neuzug.ch.</div>
  </div>
  <div class="pp" style="left:153px">
    <svg viewBox="0 0 30 22"><path d="M3 3h9l2 3h13v14H3z" fill="var(--green-dark)"/></svg>
    <div class="lbl">“Nehmen”</div>
    <div class="box">Sie erhalten <b>kostenlos qualifizierte Anfragen</b> von Abonnenten. Auf Wunsch agieren wir als Erstkontakt und <b>sammeln</b> die <b>Anfragen</b> bis zum für Sie richtigen Zeitpunkt.</div>
  </div>
  <div class="pp" style="left:212px">
    <svg viewBox="0 0 30 22"><rect x="4" y="1.5" width="22" height="15" fill="none" stroke="var(--green-dark)" stroke-width="2.4"/><rect x="13" y="16" width="4" height="3" fill="var(--green-dark)"/><rect x="9" y="19" width="12" height="2" fill="var(--green-dark)"/></svg>
    <div class="lbl">“Inserieren”</div>
    <div class="box">Vermarkten Sie Ihr Projekt effizient und kostensparend dank der Partnerschaft mit der Baufeld Portal AG. Sie erhalten ein Login &amp; ein personalisierter Auftritt mit Ihrem Logo</div>
  </div>
  <div class="pp" style="left:271px">
    <svg viewBox="0 0 30 22"><path d="M15 3l2.6 5.4 5.9.8-4.3 4.1 1 5.9L15 16.4l-5.2 2.8 1-5.9-4.3-4.1 5.9-.8z" fill="var(--green-dark)"/><g stroke="var(--green-dark)" stroke-width=".8"><line x1="15" y1="0" x2="15" y2="1.5"/><line x1="4" y1="6" x2="6" y2="7"/><line x1="26" y1="6" x2="24" y2="7"/><line x1="7" y1="21" x2="8.5" y2="19.5"/><line x1="23" y1="21" x2="21.5" y2="19.5"/></g></svg>
    <div class="lbl">“Produkte”</div>
    <div class="box">Sie möchten gerne weitere Werbemassnahmen ergreifen, um Ihr Projekt sichtbarer zu machen? Unsere Dienstleistungen finden Sie auf der Seite 6.</div>
  </div>
  <div class="p4-bar">Bei offiziellem Vermarktungsstart schalten Sie/wir Ihr Projekt kostenlos in unserem öffentlichen Bereich der Plattform frei.<br>Profitieren Sie von über &gt; <span class="green">1.5 Millionen Besuchern</span> im Jahr, welche auch ohne kostenpflichtiges Abo Ihr Projekt auffinden.</div>
  <div class="footer"><span class="mark"></span><span class="info">Baufeld Portal AG | info@baufeldportal.ch</span><span class="line"></span><span class="num">4</span></div>
</section>

<!-- Slide 5: Produkt-Übersicht -->
<section class="slide c2 r2">
  <div class="title">Produkt-Übersicht</div><div class="title-bar"></div>
  <table class="prod" style="top:46px">
    <tr><th>Produkte</th><th>Preis / Monat</th><th>Laufzeit<br>01 Monate</th><th>Preis / Monat</th><th>Laufzeit<br>03 Monate</th><th>Preis / Monat</th><th>Laufzeit<br>06 Monate</th><th>Preis / Monat</th><th>Laufzeit<br>12 Monate</th></tr>
    <tr><td>Premiumpartnerschaft</td><td>Kostenlos</td><td>In der Vorvermarktung, siehe Seite 5</td><td></td><td></td><td></td><td></td><td></td><td></td></tr>
    <tr><td>Projekt Insertion</td><td></td><td></td><td>99.-</td><td>X</td><td>79.-</td><td>X</td><td>59.-</td><td>X</td></tr>
    <tr><td>Exklusives Listing</td><td></td><td></td><td>249.-</td><td>X</td><td>199.-</td><td>X</td><td>179.-</td><td>X</td></tr>
    <tr><td>Projektshow</td><td>1490.-</td><td>X</td><td>990.-</td><td>X</td><td>890.-</td><td>X</td><td>790.-</td><td>X</td></tr>
    <tr><td>Bannerwerbung</td><td>2990.-</td><td>X</td><td>1990.-</td><td>X</td><td>1890.-</td><td>X</td><td>1790.-</td><td>X</td></tr>
  </table>
  <table class="prod" style="top:131px">
    <tr><th>Produkte</th><th>Einmalig</th><th>3er Paket</th><th>Individual<br>Offerte</th><th>Mindestpreis</th><th></th><th></th><th></th><th></th></tr>
    <tr><td>Newsletter</td><td>850.-</td><td>750.- / pro NL</td><td></td><td></td><td></td><td></td><td></td><td></td></tr>
    <tr><td>Exklusiver Newsletter</td><td></td><td></td><td>X</td><td>2000.-</td><td></td><td></td><td></td><td></td></tr>
  </table>
  <div class="footer"><span class="mark"></span><span class="info">Baufeld Portal AG | info@baufeldportal.ch</span><span class="line"></span><span class="num">5</span></div>
</section>

<!-- Slide 6: Projekt-Insertion -->
<section class="slide c3 r2">
  <div class="title">Projekt-Insertion</div><div class="title-bar"></div>
  <div class="subtitle">Inserieren Sie Ihr Projekt direkt im öffentlichen Bereich unserer Plattform</div>
  <div class="ph" role="img" aria-label="Photo: modern white villa with large windows at dusk" style="left:93px;top:54px;width:229px;height:120px;background:linear-gradient(180deg,#eef1f4 0%,#d4d6d8 40%,#5e5a55 75%,#3b3a38 100%)"></div>
  <div class="p6-sq"></div>
  <div class="p6-box">Profitieren Sie jetzt von der Publikation Ihres Neubauprojektes auf den beiden Portalen mit insgesamt über 100'000 Besuchern pro Monat sowie über 480'000 Projekt-Ansichten!</div>
  <div class="footer"><span class="mark"></span><span class="info">Baufeld Portal AG | info@baufeldportal.ch</span><span class="line"></span><span class="num">6</span></div>
</section>

<!-- Slide 7: Premium Listing -->
<section class="slide c1 r3">
  <div class="title">Premium Listing</div><div class="title-bar"></div>
  <div class="subtitle">Zusätzliche qualifizierte Kontakte - Vorreihung vor allen Gratis Projekten</div>
  <div class="shot" role="img" aria-label="Screenshot: search results grid with highlighted project listings" style="left:28px;top:52px;width:187px;height:118px;background:linear-gradient(180deg,#fafafa 0%,#eef3e2 45%,#d2d6da 100%)"></div>
  <div class="p7-dark">
    <p>Sichern Sie sich für Ihre Wohnprojekte die <span class="green">höchste Aufmerksamkeit in der für Sie relevanten Zielgruppe.</span></p>
    <p>Erhöhen Sie Ihre <span class="green">Markenbekanntheit</span> durch ihr <span class="green">exklusives Logo</span> in der Ergebnisliste.</p>
    <p>Steigern Sie <span class="green">bis zu 4-mal die Anzahl der Ansichten</span> für Ihre Projektes.</p>
  </div>
  <div class="footer"><span class="mark"></span><span class="info">Baufeld Portal AG | info@baufeldportal.ch</span><span class="line"></span><span class="num">7</span></div>
</section>

<!-- Slide 8: Premium Listing homepage -->
<section class="slide c2 r3">
  <div class="title">Premium Listing</div><div class="title-bar"></div>
  <div class="subtitle">Zusätzliche qualifizierte Kontakte - Vorreihung vor allen Gratis Projekten</div>
  <div class="shot" role="img" aria-label="Screenshot: portal homepage with bright living room and featured project" style="left:26px;top:60px;width:202px;height:105px;background:linear-gradient(90deg,#dbe9b8 0%,#f4f1ec 40%,#e8e2da 100%)"></div>
  <div class="side" style="left:242px;top:70px;width:100px">
    <p>Die <span class="green">prominenteste Platzierung</span> auf der Startseite generiert über <span class="green">65'000 Page-Views pro Monat</span></p>
    <p>Direkte Verlinkung zu Ihrer Projekt- oder Unternehmenswebsite.</p>
    <p><span class="green">Sehr hohe Wiedererkennung</span> dank Mindestlaufzeiten und Logo-Platzierungen.</p>
    <p>Max. 5 Plätze werden gleichzeitig vergeben.</p>
  </div>
  <div class="footer"><span class="mark"></span><span class="info">Baufeld Portal AG | info@baufeldportal.ch</span><span class="line"></span><span class="num">8</span></div>
</section>

<!-- Slide 9: Banner-Werbung -->
<section class="slide c3 r3">
  <div class="title">Banner-Werbung</div><div class="title-bar"></div>
  <div class="subtitle">Marken- und Imagestärkung auf allen Kauf-Ergebnislisten</div>
  <div class="shot" role="img" aria-label="Screenshot: purchase results list with banner placements" style="left:52px;top:57px;width:128px;height:109px;background:linear-gradient(180deg,#f7f7f7 0%,#e3ebd3 40%,#f5f0e3 65%,#d9dee3 100%)"></div>
  <svg class="abs" style="left:189px;top:107px" width="38" height="8" viewBox="0 0 38 8"><line x1="3" y1="4" x2="37" y2="4" stroke="var(--green)" stroke-width="1.2"/><path d="M5 1L1 4l4 3" fill="none" stroke="var(--green)" stroke-width="1.2"/></svg>
  <div class="side" style="left:237px;top:76px;width:82px">
    <p><span class="green">Bis zu 50'000 monatliche Einblendungen</span> und Sichtkontakte in allen Ergebnislisten zur <span class="green">Suche von Kaufprojekten – und Wohneinheiten.</span></p>
    <p>Es werden max. 3 Plätze gleichzeitig vergeben. Ein monatlicher Austausch Ihrer Werbebotschaft ist möglich.</p>
  </div>
  <div class="footer"><span class="mark"></span><span class="info">Baufeld Portal AG | info@baufeldportal.ch</span><span class="line"></span><span class="num">9</span></div>
</section>

</body>
</html>
```